Bluefern Healthplan

We're designing a website to sell Medicare Supplements. Attached is an image of the words we want to say and general layout, but please use your best knowledge to make it better. This platform is intentionally simplistic because this is reaching an older demographic, so it should be very straightforward, attention-grabbing and extremely user-friendly, while still appearing reliable and professional.
Use your best judgement for color palate that conveys professional but approachable. Feel free to add imagery but don't overwhelm the page.
Updates
Designs look the same
Target Market(s)
65+ seniors
Number of Pages Required
1 page
Look and feel

```html
<!DOCTYPE html>
<html lang="en">
<head>
<meta charset="utf-8">
<title>Bluefern Healthplan</title>
<link href="https://fonts.googleapis.com/css2?family=Arima:wght@400;500;600;700&family=Ubuntu:wght@500&display=swap" rel="stylesheet">
<style>
:root{
  --navy:#2d3356;
  --green:#95d43f;
  --green-soft:rgba(160,215,80,.82);
  --red:#a51d1d;
  --paper:#ffffff;
  --mist:#f4f4f4;
  --ink:#1c1c1c;
  --pink:#e23fc4;
}
*{box-sizing:border-box;margin:0;padding:0}
html,body{width:1200px;height:2183px;overflow:hidden}
body{position:relative;background:var(--paper);font-family:"Arima",serif;color:var(--ink)}
.abs{position:absolute}

/* hero */
.hero{left:0;top:0;width:1200px;height:596px;overflow:hidden}
.hero-photo{left:0;top:0;width:1200px;height:596px;
  background:linear-gradient(100deg,#7a6a55 0%,#b59c7e 30%,#d7c3a8 48%,#8b6f55 70%,#5b4a3c 100%)}
.topbar{left:0;top:0;width:1200px;height:97px;background:rgba(40,40,40,.72)}
.brand{left:112px;top:26px;font-family:"Arima",serif;font-weight:700;font-size:34px;color:#fff}
.nav{left:446px;top:35px;display:flex;gap:46px;font-family:"Ubuntu",sans-serif;font-weight:500;font-size:17px;color:#fff}
.nav a{color:#fff;text-decoration:none;position:relative}
.nav a.active::after{content:"";position:absolute;left:-10px;right:-12px;bottom:-8px;height:3px;background:var(--green);border-radius:2px}
.account{left:950px;top:39px;display:flex;align-items:center;gap:6px;font-family:"Ubuntu",sans-serif;font-weight:500;font-size:14px;color:#fff}
.account .sep{color:var(--green)}
.hero-band{left:0;top:197px;width:1200px;height:263px;
  background:linear-gradient(90deg,var(--green-soft) 0%,var(--green-soft) 62%,rgba(160,215,80,0) 80%)}
.hero-title{left:112px;top:226px;font-size:43px;font-weight:700;color:var(--navy);letter-spacing:.3px}
.hero-sub{left:113px;top:290px;font-size:26px;font-weight:600;color:#fff;line-height:35px}
.hero-dial{left:113px;top:380px;font-size:17px;font-weight:600;color:var(--navy)}
.hero-dial b{font-size:31px;color:var(--red);font-weight:600;margin-right:6px}

/* intro */
.intro{left:112px;top:650px;width:975px;height:176px;background:var(--green);border-radius:16px;text-align:center;padding-top:20px}
.intro p{font-size:17px;line-height:29px;font-weight:500}
.intro .cta{margin-top:12px;font-size:21px;line-height:29px;font-weight:600}

/* quiz */
.quiz{left:293px;top:871px;width:615px;height:395px;background:var(--navy);border-radius:18px;box-shadow:0 2px 4px rgba(0,0,0,.25)}
.quiz-step{left:33px;top:42px;font-size:20px;color:#fff}
.quiz-q{left:0;width:615px;top:52px;text-align:center;font-size:36px;font-weight:600;color:var(--green)}
.opt{left:0;width:615px;height:36px}
.opt .letter{position:absolute;left:84px;top:0;font-size:30px;font-weight:600;color:var(--green);line-height:36px}
.opt .radio{position:absolute;left:131px;top:1px;width:34px;height:34px;border-radius:50%;background:#fff;border:3px solid var(--green)}
.opt .pill{position:absolute;left:177px;top:0;width:352px;height:36px;background:#fff;border-radius:7px;box-shadow:inset 0 -3px 4px rgba(0,0,0,.18);font-size:18px;line-height:38px;padding-left:17px;color:#222}
.btn-next{left:219px;top:282px;width:176px;height:44px;border-radius:22px;background:var(--green);color:var(--navy);font-size:22px;font-weight:600;text-align:center;line-height:46px}

/* info */
.info{left:0;top:1312px;width:1200px;height:484px;background:var(--mist);padding:40px 113px 0}
.info h2{font-size:18px;font-weight:600;color:var(--navy);margin-bottom:14px}
.info p{font-size:11.6px;line-height:17.6px;color:var(--navy)}
.info ul{list-style:none;margin:18px 0 16px 30px}
.info li{font-size:11.6px;line-height:17.6px;color:var(--navy);padding-left:16px;position:relative}
.info li::before{content:"";position:absolute;left:0;top:3px;width:11px;height:11px;border-radius:50%;background:var(--navy)}

/* footer */
.footer{left:0;top:1796px;width:1200px;height:387px;background:var(--navy);color:var(--green)}
.f-brand{left:138px;top:52px;font-size:32px;font-weight:700}
.f-about{left:138px;top:115px;width:270px;font-size:12.5px;line-height:22px;font-weight:500}
.f-social{left:138px;top:262px;display:flex;gap:26px}
.f-social span{width:21px;height:21px;border-radius:50%;background:var(--green)}
.f-h{font-size:26px;font-weight:600;letter-spacing:1.5px}
.f-links{left:568px;top:115px;list-style:none;font-size:18px;letter-spacing:1.5px;line-height:30.7px;font-weight:500}
.f-links li:first-child{color:var(--pink)}
.f-contact{left:836px;top:122px;font-size:18px;letter-spacing:1.5px;font-weight:500;line-height:30.7px}
.f-contact .row{display:flex;gap:10px;align-items:flex-start;margin-bottom:4px}
.f-contact svg{margin-top:7px;flex:none}
.f-rule{left:112px;top:336px;width:975px;height:1px;background:rgba(255,255,255,.35)}
.f-copy{left:0;width:1200px;top:355px;text-align:center;font-size:11px;letter-spacing:.8px;color:#fff}
</style>
</head>
<body>

<section class="abs hero">
  <div class="abs hero-photo" role="img" aria-label="Photo of smiling seniors sharing fruit and wine around a table"></div>
  <div class="abs topbar"></div>
  <div class="abs brand">Bluefern Healthplan</div>
  <nav class="abs nav">
    <a class="active" href="#">Home</a>
    <a href="#">About Us</a>
    <a href="#">Learn about medicare</a>
  </nav>
  <div class="abs account">
    <svg width="12" height="14" viewBox="0 0 12 14"><rect x="1" y="6" width="10" height="8" rx="1" fill="#95d43f"/><path d="M3 6V4a3 3 0 0 1 6 0v2" fill="none" stroke="#95d43f" stroke-width="2"/></svg>
    <span>Login</span><span class="sep">|</span><span>Register</span>
  </div>
  <div class="abs hero-band"></div>
  <h1 class="abs hero-title">Welcome to Bluefern Healthplan</h1>
  <p class="abs hero-sub">Be confident in choosing the Medicare<br>Supplement plan that’s right for you.</p>
  <p class="abs hero-dial"><b>Dial (800) 555-0142</b>to talk to a live agent</p>
</section>

<section class="abs intro">
  <p>We know insurance can be confusing. With so much information and not enough answers, we’re<br>here to help you find the plan that works best for you, your family and your health.</p>
  <p class="cta">Take this short quiz to find flexible and<br>affordable plans that you can feel confident in.</p>
</section>

<section class="abs quiz">
  <div class="abs quiz-step">1/4</div>
  <h2 class="abs quiz-q">Q1. I am</h2>
  <div class="abs opt" style="top:229px;top:110px">
    <span class="letter">a :</span>
    <svg class="radio" style="border:none;background:none" width="36" height="36" viewBox="0 0 36 36">
      <circle cx="18" cy="18" r="16" fill="#fff" stroke="#2d3356" stroke-width="2"/>
      <circle cx="18" cy="18" r="11" fill="#3aa0dc"/>
      <circle cx="18" cy="18" r="7" fill="#fff"/>
      <circle cx="18" cy="18" r="3.5" fill="#3aa0dc"/>
      <path d="M18 18 L31 5" stroke="#2d3356" stroke-width="2"/>
      <path d="M28 4 l4 0 l0 4" fill="none" stroke="#95d43f" stroke-width="2"/>
    </svg>
    <span class="pill">Over 64 years old</span>
  </div>
  <div class="abs opt" style="top:164px">
    <span class="letter">b :</span><span class="radio"></span>
    <span class="pill">64 years old</span>
  </div>
  <div class="abs opt" style="top:218px">
    <span class="letter">c :</span><span class="radio"></span>
    <span class="pill">Under 64 years old</span>
  </div>
  <div class="abs btn-next">Next Question</div>
</section>

<section class="abs info">
  <h2>What is a Medicare Supplement plan?</h2>
  <p>Each Medicare Supplement insurance plan offers a different level of basic benefits, but each lettered plan will include the same standardized basic benefits regardless of insurance company and location. Medicare Supplement insurance plans do not always cover vision, dental, long-term care, or hearing aids, but all plans must cover at least a portion of the following basic benefits:</p>
  <ul>
    <li>Medicare Part A coinsurance costs up to an additional 365 days after Medicare benefits are exhausted</li>
    <li>Medicare Part A hospice care coinsurance or copayments</li>
    <li>Medicare Part B coinsurance or copayments</li>
    <li>First three pints of blood used in a medical procedure</li>
  </ul>
  <h2>Medicare Supplement insurance plan costs</h2>
  <p>Although private insurance companies are required to offer the same basic benefits for each lettered plan, they do have the ability to charge different premiums. You might want to shop around to find a Medicare Supplement insurance plan that may fit your medical and financial needs. Insurance companies may price their plan premiums in any of the following ways:</p>
  <ul>
    <li>Community no-age-rated: These Medicare Supplement insurance plans charge premiums that are the same across the board, regardless of age.</li>
    <li>Issue-age-rated: These plans base their premiums on your age when you first enrolled in the policy. Therefore, the younger you are when you enroll in this type of plan, the lower your premium will be.</li>
    <li>Attained-age-rated: Like issue-age-rated, these plans base their premiums on the age you were when you first bought a policy, but unlike issue-age-rated, premiums increase as you get older. Please note that no matter what rating method an insurance company uses, premiums may increase over time for reasons other than age, such as inflation.</li>
  </ul>
</section>

<footer class="abs footer">
  <div class="abs f-brand">Bluefern Healthplan</div>
  <p class="abs f-about">Lorem ipsum dolor sit amet, conse ctetur adipiscing elit, sed do eiusmod tempor incididunt ut labore et dolore magna aliqua. Quis ipsum suspendisse ultrices gravida. Risus commodo vive rra maecenas accumsan lacus vel facilisis.</p>
  <div class="abs f-social"><span></span><span></span><span></span><span></span></div>

  <div class="abs f-h" style="left:573px;top:56px">Link</div>
  <ul class="abs f-links">
    <li>About</li><li>Blog</li><li>Privecy Policy</li><li>Terms</li><li>Cokies</li><li>Site map</li>
  </ul>

  <div class="abs f-h" style="left:857px;top:68px">Contact Us</div>
  <div class="abs f-contact">
    <div class="row">
      <svg width="17" height="17" viewBox="0 0 17 17"><rect width="17" height="17" rx="2" fill="#95d43f"/><path d="M5 4l2 0 1 3-1.5 1a6 6 0 0 0 3 3l1-1.5 3 1 0 2c-5 1-9-3-9-8z" fill="#2d3356"/></svg>
      <span>(800) 555-0142</span>
    </div>
    <div class="row">
      <svg width="20" height="16" viewBox="0 0 20 16"><rect x="1" y="2" width="18" height="12" rx="1" fill="#95d43f"/><path d="M1 3l9 6 9-6" fill="none" stroke="#2d3356" stroke-width="1.6"/></svg>
      <span>hello@bluefernhealth.com</span>
    </div>
    <div class="row">
      <svg width="18" height="18" viewBox="0 0 18 18"><path d="M17 1L1 8l7 2 2 7z" fill="#95d43f"/></svg>
      <span>12 Maple Grove Road,<br>Fernwood, CA,<br>90211</span>
    </div>
  </div>

  <div class="abs f-rule"></div>
  <div class="abs f-copy">© 2020 Bluefernhealthplan.com. All Rights reserved</div>
</footer>

</body>
</html>
```